Holistic/ Sports Psychologist needs flyer design

I need a flyer designed that catches the attention of potential customers - (parents of young athletes and athletes) who may be looking for psychological services. I have a logo and all the relevant info for the flyer but would like someone to take it and make it look creative, fun, fresh and attention getting for high school and college athletes. The colors used can be from my logo design which represents my holistic approach.
Target Market(s)
high school and collegiate athletes
Industry/Entity Type
sports psychology
Requirements
Must have
- Info I put on the flyer with my logo and please add some graphics and color based on my logo

```html
<!DOCTYPE html>
<html lang="en">
<head>
<meta charset="utf-8">
<title>Holistic &amp; Sports Psychology Consulting Flyer</title>
<link href="https://fonts.googleapis.com/css2?family=Kalam:wght@400;700&family=Open+Sans:ital,wght@0,400;0,600;0,700;1,400;1,600&display=swap" rel="stylesheet">
<style>
  :root {
    --page-bg: #e9ecee;
    --paper: #ffffff;
    --blue: #1f63a8;
    --blue-dark: #164a82;
    --green: #8cc63f;
    --green-dark: #5fa52e;
    --ink: #4a4f55;
    --soft: #f2f7ec;
    --photo-a: #c9e0ef;
    --photo-b: #e4ecdf;
  }
  * { box-sizing: border-box; margin: 0; padding: 0; }
  html, body { width: 1200px; height: 2212px; overflow: hidden; }
  body {
    background: var(--page-bg);
    font-family: "Open Sans", Arial, sans-serif;
    color: var(--ink);
    position: relative;
  }
  .flyer {
    position: absolute;
    left: 40px; top: 381px;
    width: 1120px; height: 1450px;
    background: var(--paper);
    overflow: hidden;
    box-shadow: 0 6px 24px rgba(0,0,0,.12);
  }
  .corner-swoosh { position: absolute; left: 0; top: 0; }
  .brand {
    position: absolute; left: 56px; top: 48px;
    display: flex; align-items: center; gap: 14px;
    padding: 14px 26px;
    border: 2px solid var(--green);
    border-radius: 10px;
    background: var(--paper);
  }
  .brand-dot { width: 22px; height: 22px; border-radius: 50%; background: var(--green); }
  .brand-name { font-weight: 600; font-size: 30px; color: var(--blue); }
  .hero-photo {
    position: absolute; left: 660px; top: 20px;
    width: 420px; height: 420px; border-radius: 50%;
    background: linear-gradient(160deg, var(--photo-a) 0%, var(--photo-b) 100%);
    border: 14px solid var(--paper);
    box-shadow: 0 0 0 10px var(--green), 0 0 0 20px var(--blue);
  }
  .title-band {
    position: absolute; left: 0; top: 200px;
    width: 700px; height: 230px;
    background: linear-gradient(90deg, var(--green) 0%, var(--green-dark) 45%, var(--blue) 100%);
    border-radius: 0 120px 0 0;
    padding: 30px 0 0 56px;
  }
  .title-band h1 {
    font-family: "Kalam", cursive;
    font-weight: 700; font-size: 52px; line-height: 1.08;
    color: #fff;
  }
  .headline {
    position: absolute; left: 0; top: 490px; width: 100%;
    text-align: center; color: var(--blue);
    font-weight: 700; font-size: 34px; line-height: 1.3;
  }
  .services {
    position: absolute; left: 40px; top: 610px; width: 1040px;
    display: flex; justify-content: space-between;
  }
  .service {
    width: 196px; height: 370px; text-align: center;
    background: var(--soft);
    border-top: 6px solid var(--green);
    border-radius: 8px;
    padding: 24px 14px 22px;
  }
  .service-icon {
    width: 90px; height: 90px; border-radius: 50%;
    background: var(--blue); margin: 0 auto 16px;
    display: flex; align-items: center; justify-content: center;
  }
  .service h3 { color: var(--blue); font-size: 20px; line-height: 1.2; margin-bottom: 12px; }
  .service p { font-size: 15px; line-height: 1.45; }
  .about {
    position: absolute; left: 0; top: 1010px; width: 100%; height: 310px;
    background: linear-gradient(90deg, #eef5f9, #f4f9ee);
  }
  .portrait {
    position: absolute; left: 56px; top: 20px;
    width: 320px; height: 270px; border-radius: 8px;
    background: linear-gradient(160deg, #cfe3f1 0%, #d6e6d0 100%);
    border: 6px solid var(--paper);
  }
  .about-text {
    position: absolute; left: 410px; top: 28px; width: 660px;
    font-size: 17px; line-height: 1.55;
  }
  .about-text p + p { margin-top: 12px; }
  .telehealth {
    position: absolute; left: 410px; top: 238px; width: 660px; height: 50px;
    background: var(--green); color: #fff; border-radius: 25px;
    display: flex; align-items: center; justify-content: center;
    font-style: italic; font-weight: 600; font-size: 17px;
  }
  .footer {
    position: absolute; left: 0; bottom: 0; width: 100%; height: 100px;
    background: var(--blue);
    display: flex; align-items: center; justify-content: space-between;
    padding: 0 56px; color: #fff;
  }
  .phone { display: flex; align-items: center; gap: 12px; font-weight: 700; font-size: 30px; }
  .web { font-weight: 600; font-size: 22px; }
  .address { font-size: 17px; line-height: 1.35; text-align: right; }
</style>
</head>
<body>
  <main class="flyer">
    <svg class="corner-swoosh" width="420" height="60" viewBox="0 0 420 60" aria-hidden="true">
      <path d="M0 18 C140 40 260 20 420 0 L0 0 Z" fill="var(--green)"/>
      <path d="M0 28 C150 50 270 26 420 6" stroke="var(--blue)" stroke-width="4" fill="none"/>
    </svg>

    <div class="brand">
      <span class="brand-dot"></span>
      <span class="brand-name">Dr. Elena Whitfield</span>
    </div>

    <div class="hero-photo" role="img" aria-label="Photo of a family walking with a dog on a sunny beach"></div>

    <div class="title-band">
      <h1>Holistic Psychology<br>&amp; Sports Psychology<br>Consulting</h1>
    </div>

    <h2 class="headline">Ways to Improve Athletic<br>Performance Using Sports and Holistic Psychology</h2>

    <section class="services">
      <article class="service">
        <div class="service-icon">
          <svg width="50" height="50" viewBox="0 0 50 50" aria-hidden="true"><circle cx="25" cy="25" r="20" stroke="#fff" stroke-width="4" fill="none"/><circle cx="25" cy="25" r="11" stroke="#fff" stroke-width="4" fill="none"/><circle cx="25" cy="25" r="3" fill="#fff"/></svg>
        </div>
        <h3>Mental Skills Training</h3>
        <p>Visualization, goal setting, motivation, self-talk, focus and concentration techniques</p>
      </article>
      <article class="service">
        <div class="service-icon">
          <svg width="50" height="50" viewBox="0 0 50 50" aria-hidden="true"><path d="M6 40 L18 28 L26 34 L42 14" stroke="#fff" stroke-width="4" fill="none"/><path d="M32 12 H44 V24" stroke="#fff" stroke-width="4" fill="none"/></svg>
        </div>
        <h3>Performance Enhancement</h3>
        <p>Overcome psychological barriers that are holding you back such as fear, anxiety, perfectionism, lack of focus</p>
      </article>
      <article class="service">
        <div class="service-icon">
          <svg width="50" height="50" viewBox="0 0 50 50" aria-hidden="true"><path d="M25 42 L8 25 A9 9 0 0 1 25 13 A9 9 0 0 1 42 25 Z" fill="#fff"/></svg>
        </div>
        <h3>Mental Health</h3>
        <p>Anxiety and stress management, mood regulation techniques, mindfulness and relaxation practices</p>
      </article>
      <article class="service">
        <div class="service-icon">
          <svg width="50" height="50" viewBox="0 0 50 50" aria-hidden="true"><path d="M19 8 H31 V19 H42 V31 H31 V42 H19 V31 H8 V19 H19 Z" fill="#fff"/></svg>
        </div>
        <h3>Injury Recovery Support</h3>
        <p>Assist athletes in maintaining resilience and positive mental outlook while processing emotions related to injury and recovery</p>
      </article>
      <article class="service">
        <div class="service-icon">
          <svg width="50" height="50" viewBox="0 0 50 50" aria-hidden="true"><path d="M25 8 V42 M14 42 H36 M8 16 H42" stroke="#fff" stroke-width="4" fill="none"/><path d="M8 16 L3 28 H13 Z M42 16 L37 28 H47 Z" fill="#fff"/></svg>
        </div>
        <h3>Burnout Prevention</h3>
        <p>Teach athletes how to have balance in sports and life so they can continue to enjoy the sport they love</p>
      </article>
    </section>

    <section class="about">
      <div class="portrait" role="img" aria-label="Photo of the psychologist sitting outdoors with her dog"></div>
      <div class="about-text">
        <p>Dr. Elena Whitfield is a licensed psychologist who combines evidence-based sports psychology with holistic practices to help high school and college athletes perform at their best, manage pressure, and enjoy their sport.</p>
        <p>Her specializations include confidence, performance anxiety, stress management, focus, motivation, injury recovery, and healthy balance between athletics, academics and life.</p>
      </div>
      <div class="telehealth">All services are provided online via telehealth &nbsp;|&nbsp; Sessions are 50 to 55 minutes</div>
    </section>

    <footer class="footer">
      <div class="phone">
        <svg width="30" height="30" viewBox="0 0 24 24" aria-hidden="true"><path d="M6.6 10.8a15.1 15.1 0 0 0 6.6 6.6l2.2-2.2a1 1 0 0 1 1-.25 11.4 11.4 0 0 0 3.6.57 1 1 0 0 1 1 1V20a1 1 0 0 1-1 1A17 17 0 0 1 3 4a1 1 0 0 1 1-1h3.5a1 1 0 0 1 1 1c0 1.25.2 2.45.57 3.57a1 1 0 0 1-.25 1z" fill="#fff"/></svg>
        904-555-0182
      </div>
      <div class="web">www.drelenawhitfield.com</div>
      <div class="address">214 Harbor Lane #118<br>Seabrook Beach, FL 32000</div>
    </footer>
  </main>
</body>
</html>
```